Home Security and Smart Home Flyer

A professional flyer to Hand out to people to get them interested in our service, also have a special promotion on it. Have our product on it. We are a home security company and our goal is to get as many clients as possible with great deals to protect we also provide smart home automation products

Target Market(s)

Anyone Owns a home. Anyone that currently has the old alarm

Industry/Entity Type

Security Service

Font styles to use
Sans Serif

Colors
33a6d7
ec1f27
0255a3
ffffff
0393ce
85cae6
cee9f5
3276b5
85acd3

Requirements
Must have
• The alarm panel, doorbell camera. Our monthly rate starting as low as 29.99. Free Sameday installation, Free Equipment. Our Bright Harbor logo. And bright harbor on anything that has to do with the company. Phone number 8004172396. Website www.brightharborhome.example. Needs to be double sided.
• Free Doorbell Camera
• Free Installation
• Free Smart Home Security System
• Arizona Preferred Choice
• Award-winning service
• Best deal out there guaranteed
• “You find someone out there better will beat it”
Nice to have
• Imagine you on your home and you were wanting me to get a really cool system in your home watch with me you shoes instead of other people design the flyer around that make it look really interesting so they want to call back with the great offers were already presented to them
Should not have
• Do not have anything that says Kov on it or Palvex on it.

```html
<!DOCTYPE html>
<html lang="en">
<head>
<meta charset="utf-8">
<title>Bright Harbor – Home Security Flyer</title>
<link rel="stylesheet" href="https://fonts.googleapis.com/css2?family=Open+Sans:wght@300;400;600;700&display=swap">
<style>
  :root {
    --navy: #0d4a78;
    --cyan: #33a6d7;
    --cyan-deep: #0393ce;
    --pale: #cee9f5;
    --sky: #85cae6;
    --ink: #3a3f45;
    --muted: #5d6a75;
    --white: #ffffff;
    --stage: #e6e7e9;
  }
  * { box-sizing: border-box; margin: 0; padding: 0; }
  html, body { width: 1200px; height: 836px; overflow: hidden; }
  body { background: var(--stage); font-family: "Open Sans", Arial, sans-serif; color: var(--ink); position: relative; }

  .page { position: absolute; top: 114px; width: 499px; height: 646px; background: #f4f5f6; overflow: hidden; box-shadow: 0 2px 8px rgba(0,0,0,.18); }
  .page--front { left: 86px; }
  .page--back { left: 627px; }
  .page__shapes { position: absolute; inset: 0; }
  .abs { position: absolute; }

  /* front */
  .brand { left: 35px; top: 44px; display: flex; align-items: center; gap: 8px; font-weight: 300; font-size: 25px; letter-spacing: 4px; color: var(--navy); }
  .brand__mark { width: 12px; height: 12px; background: var(--cyan); }
  .tagline { left: 32px; top: 123px; color: var(--white); font-size: 10.5px; letter-spacing: 1.2px; line-height: 15px; font-weight: 400; }
  .front-title { left: 198px; top: 290px; font-size: 14px; font-weight: 700; color: var(--navy); letter-spacing: -.1px; }
  .front-copy { left: 198px; top: 312px; width: 282px; font-size: 10.2px; line-height: 13px; text-align: justify; color: var(--ink); }
  .feature { display: flex; align-items: center; gap: 9px; font-size: 12px; color: var(--ink); }
  .feature svg { width: 31px; height: 31px; }
  .perks { font-size: 12px; line-height: 20.5px; color: var(--ink); }
  .offer { left: 362px; top: 468px; width: 124px; height: 140px; }
  .offer__text { position: absolute; inset: 0; display: flex; align-items: center; justify-content: center; text-align: center; color: var(--white); font-weight: 600; font-size: 14px; line-height: 18.5px; }
  .contact { width: 499px; text-align: center; color: var(--white); }
  .contact__cta { top: 580px; left: 60px; width: 380px; font-size: 11.5px; color: var(--cyan); }
  .contact__phone { font-size: 14px; letter-spacing: 2px; display: flex; justify-content: center; align-items: center; gap: 8px; }
  .contact__web { font-size: 13px; letter-spacing: 1.6px; }
  .socials { left: 378px; top: 616px; display: flex; gap: 5px; }
  .socials span { width: 19px; height: 19px; border-radius: 50%; background: #b9c3cb; display: block; }

  /* back */
  .back-title { top: 174px; width: 499px; text-align: center; font-size: 15.5px; font-weight: 700; color: var(--navy); }
  .back-copy { left: 20px; top: 205px; width: 459px; text-align: center; font-size: 10.1px; line-height: 13px; color: var(--ink); }
  .device-grid { left: 14px; top: 284px; display: grid; grid-template-columns: repeat(5, 92.6px); grid-auto-rows: 58.5px; gap: 1.6px; }
  .device-tile { background: var(--navy); color: var(--white); display: flex; flex-direction: column; align-items: center; justify-content: center; gap: 6px; font-size: 7.4px; text-align: center; }
  .device-tile svg { width: 16px; height: 16px; fill: var(--white); }
  .partners { left: 26px; top: 488px; display: flex; align-items: center; gap: 14px; }
  .partners span { display: block; background: #c5ccd2; }
</style>
</head>
<body>

<!-- Front side -->
<section class="page page--front">
  <svg class="page__shapes" viewBox="0 0 499 646" width="499" height="646">
    <defs>
      <linearGradient id="familyTone" x1="0" x2="1" y1="0" y2="0">
        <stop offset="0" stop-color="#f6f5f3"/>
        <stop offset=".35" stop-color="#eee6dc"/>
        <stop offset=".7" stop-color="#c8ab92"/>
        <stop offset="1" stop-color="#9a8a7e"/>
      </linearGradient>
      <linearGradient id="phoneTone" x1="0" x2="0" y1="0" y2="1">
        <stop offset="0" stop-color="#eef0f2"/>
        <stop offset="1" stop-color="#cfd5da"/>
      </linearGradient>
    </defs>
    <g role="img" aria-label="Photo of a smiling family on a sofa looking at a tablet, with an indoor security camera">
      <polygon points="0,0 499,0 499,196 183,270 0,205" fill="url(#familyTone)"/>
    </g>
    <polyline points="0,205 183,270 499,196" fill="none" stroke="var(--cyan)" stroke-width="4"/>
    <polygon points="0,118 227,118 227,130 219,153 0,153" fill="var(--cyan)"/>

    <polygon points="0,490 320,575 0,650" fill="var(--pale)"/>
    <polygon points="0,622 499,470 499,646 0,646" fill="var(--white)"/>
    <polygon points="0,630 499,478 499,646 0,646" fill="var(--navy)"/>

    <g role="img" aria-label="Smartphone showing the home automation app">
      <rect x="27" y="192" width="149" height="293" rx="20" fill="url(#phoneTone)" stroke="#b8c0c7"/>
    </g>
  </svg>

  <div class="abs brand"><span class="brand__mark"></span>BRIGHT HARBOR</div>
  <div class="abs tagline">FEEL SECURE &amp; SAFE WITH<br>BRIGHT HARBOR</div>

  <h2 class="abs front-title">YOU'RE CHARGE WITH HOME AUTOMATION</h2>
  <p class="abs front-copy">Now you can manage your security system and your home via smartphone, tablet or computer. Whether you're on the couch or on the beach, take advantage of the latest smart-home equipment to enhance your safety and your lifestyle. Let us show you how smart your home can realy be.</p>

  <div class="abs feature" style="left:198px;top:395px">
    <svg viewBox="0 0 31 31"><circle cx="15.5" cy="15.5" r="14" fill="#e9edf0" stroke="#4f6272" stroke-width="1.5"/><rect x="9" y="11" width="13" height="10" fill="none" stroke="#4f6272" stroke-width="1.4"/><line x1="9" y1="14.5" x2="22" y2="14.5" stroke="#4f6272"/><line x1="9" y1="17.5" x2="22" y2="17.5" stroke="#4f6272"/></svg>GARAGE DOOR</div>
  <div class="abs feature" style="left:346px;top:395px">
    <svg viewBox="0 0 31 31"><circle cx="15.5" cy="15.5" r="14" fill="#e9edf0" stroke="#4f6272" stroke-width="1.5"/><circle cx="15.5" cy="13" r="5" fill="none" stroke="#4f6272" stroke-width="1.4"/><rect x="13" y="18" width="5" height="4" fill="#4f6272"/></svg>LIGHTS</div>
  <div class="abs feature" style="left:198px;top:433px">
    <svg viewBox="0 0 31 31"><circle cx="15.5" cy="15.5" r="14" fill="#e9edf0" stroke="#4f6272" stroke-width="1.5"/><circle cx="12" cy="12" r="3.5" fill="#4f6272"/><line x1="13" y1="13" x2="21" y2="21" stroke="#4f6272" stroke-width="2.5"/></svg>DOOR LOCKS</div>
  <div class="abs feature" style="left:346px;top:433px">
    <svg viewBox="0 0 31 31"><circle cx="15.5" cy="15.5" r="14" fill="#e9edf0" stroke="#4f6272" stroke-width="1.5"/><polygon points="12,10 22,15.5 12,21" fill="#4f6272"/></svg>VIDEO</div>

  <div class="abs perks" style="left:24px;top:537px">Free Same day installation<br>Free Equipment</div>

  <div class="abs offer">
    <svg viewBox="0 0 124 140" width="124" height="140"><polygon points="62,3 121,36 121,104 62,137 3,104 3,36" fill="var(--cyan)" stroke="var(--white)" stroke-width="3"/></svg>
    <div class="offer__text">OUR MONTHLY<br>RATE STARTING<br>AS LOW AS<br>$29.99</div>
  </div>

  <div class="abs contact contact__cta">Contact Bright Harbor today for a free quote.</div>
  <div class="abs contact contact__phone" style="top:597px;left:-3px">
    <svg width="15" height="15" viewBox="0 0 16 16"><circle cx="8" cy="8" r="7" fill="none" stroke="#fff" stroke-width="1.4"/><path d="M5.5 4.5l1.5 0 .6 1.8-.9.8a5 5 0 0 0 2.2 2.2l.8-.9 1.8.6v1.5c-3.5.3-6.3-2.5-6-6z" fill="#fff"/></svg>
    8004172396</div>
  <div class="abs contact contact__web" style="top:617px;left:-3px">www.brightharborhome.example</div>
  <div class="abs socials"><span></span><span></span><span></span><span></span></div>
</section>

<!-- Back side -->
<section class="page page--back">
  <svg class="page__shapes" viewBox="0 0 499 646" width="499" height="646">
    <defs>
      <linearGradient id="houseTone" x1="0" x2="0" y1="0" y2="1">
        <stop offset="0" stop-color="#6d7f91"/>
        <stop offset=".5" stop-color="#a59a8a"/>
        <stop offset="1" stop-color="#5f5a50"/>
      </linearGradient>
      <linearGradient id="handTone" x1="0" x2="1">
        <stop offset="0" stop-color="#e6c4a8"/>
        <stop offset="1" stop-color="#c99b7c"/>
      </linearGradient>
    </defs>
    <g role="img" aria-label="Photo of a modern two-storey house at dusk with an outdoor security camera in front">
      <polygon points="0,0 499,0 499,82 254,155 0,82" fill="url(#houseTone)"/>
      <rect x="18" y="20" width="98" height="150" rx="10" fill="#eef0f2" opacity=".85"/>
    </g>
    <polyline points="0,86 254,159 499,86" fill="none" stroke="var(--white)" stroke-width="3"/>
    <polyline points="0,90 254,163 499,90" fill="none" stroke="var(--cyan)" stroke-width="3"/>

    <polygon points="0,530 330,580 0,640" fill="var(--pale)"/>
    <polygon points="0,617 499,490 499,646 0,646" fill="var(--white)"/>
    <polygon points="0,625 499,498 499,646 0,646" fill="var(--navy)"/>

    <g role="img" aria-label="Photo of a hand holding a smartphone showing live security video">
      <rect x="383" y="468" width="86" height="150" rx="12" fill="#eef0f2" stroke="#b8c0c7" transform="rotate(12 426 543)"/>
      <rect x="360" y="560" width="70" height="86" rx="20" fill="url(#handTone)"/>
    </g>
  </svg>

  <h2 class="abs back-title">Protect Your Home With a Bright Harbor Security System</h2>
  <p class="abs back-copy">You deserve a safe and secure home for yourself and your loved ones. We offer our home security systems with live monitoring - featuring our 24-hour award-winning Alarm Response Center. Equipment to protect against fire, smoke, carbon monoxide, and flood and freeze events. Your home should be a sanctuary that provides refuge and the peace of mind you deserve.</p>

  <div class="abs device-grid">
    <div class="device-tile"><svg viewBox="0 0 16 16"><rect x="1" y="4" width="10" height="8" rx="1"/><polygon points="11,8 15,5 15,11"/></svg>Video Cameras</div>
    <div class="device-tile"><svg viewBox="0 0 16 16"><rect x="2" y="4" width="12" height="10" rx="2"/><rect x="6" y="2" width="4" height="3" fill="none" stroke="#fff"/></svg>Medical Pendant/Watch</div>
    <div class="device-tile"><svg viewBox="0 0 16 16"><rect x="2" y="3" width="6" height="11" rx="2"/><circle cx="12" cy="5" r="2.5"/></svg>Keychain Remote</div>
    <div class="device-tile"><svg viewBox="0 0 16 16"><circle cx="8" cy="6" r="5"/><rect x="6" y="11" width="4" height="4"/></svg>Light/Appliance Module</div>
    <div class="device-tile"><svg viewBox="0 0 16 16"><text x="8" y="13" font-size="11" font-weight="700" text-anchor="middle" fill="#fff" font-family="Open Sans, sans-serif">CO</text></svg>Co Detector</div>
    <div class="device-tile"><svg viewBox="0 0 16 16"><rect x="3" y="7" width="10" height="8" rx="1"/><path d="M5 7V5a3 3 0 0 1 6 0v2" fill="none" stroke="#fff" stroke-width="1.6"/></svg>Door Locks</div>
    <div class="device-tile"><svg viewBox="0 0 16 16"><rect x="6.5" y="1" width="3" height="10" rx="1.5"/><circle cx="8" cy="12.5" r="3"/></svg>Thermostats</div>
    <div class="device-tile"><svg viewBox="0 0 16 16"><path d="M8 1C6 5 3.5 8 3.5 10.5a4.5 4.5 0 0 0 9 0C12.5 8 10 5 8 1z"/></svg>Moisture Sensor</div>
    <div class="device-tile"><svg viewBox="0 0 16 16"><rect x="5" y="2" width="6" height="12" rx="1"/><path d="M3 5v6M13 5v6" stroke="#fff" fill="none"/></svg>Shock Sensor</div>
    <div class="device-tile"><svg viewBox="0 0 16 16"><path d="M1 3h14v3a7 4 0 0 1-14 0z"/><circle cx="6" cy="12" r="1"/><circle cx="10" cy="12" r="1"/><circle cx="8" cy="14" r="1"/></svg>Smoke Detector</div>
    <div class="device-tile"><svg viewBox="0 0 16 16"><text x="8" y="13" font-size="11" font-weight="700" text-anchor="middle" fill="#fff" font-family="Open Sans, sans-serif">F°</text></svg>Heat Detector</div>
    <div class="device-tile"><svg viewBox="0 0 16 16"><rect x="1" y="4" width="14" height="10" rx="1.5"/><circle cx="8" cy="9" r="3" fill="#0d4a78"/><rect x="5" y="2" width="6" height="2"/></svg>Image Sensor</div>
    <div class="device-tile"><svg viewBox="0 0 16 16"><path d="M8 1v14M1 8h14M3 3l10 10M13 3L3 13" stroke="#fff" stroke-width="1.2"/></svg>Glass Break Detector</div>
    <div class="device-tile"><svg viewBox="0 0 16 16"><path d="M8 1v14M2 4.5l12 7M14 4.5l-12 7" stroke="#fff" stroke-width="2"/></svg>Freeze Sensor</div>
    <div class="device-tile"><svg viewBox="0 0 16 16"><path d="M1 6l7-4 7 4v9H1z"/><rect x="4" y="8" width="8" height="7" fill="#0d4a78"/><path d="M4 10h8M4 12.5h8" stroke="#fff"/></svg>Garage Sensor</div>
  </div>

  <div class="abs partners">
    <span style="width:34px;height:18px;border-radius:3px"></span>
    <span style="width:46px;height:18px;border-radius:3px"></span>
    <span style="width:22px;height:22px;border-radius:50%"></span>
    <span style="width:22px;height:22px;border-radius:50%"></span>
    <span style="width:62px;height:14px;border-radius:3px"></span>
    <span style="width:52px;height:18px;border-radius:3px"></span>
    <span style="width:24px;height:24px;border-radius:50%"></span>
  </div>

  <div class="abs perks" style="left:24px;top:552px">Free Same day installation<br>Free Equipment</div>

  <div class="abs contact contact__phone" style="top:612px;left:0">
    <svg width="15" height="15" viewBox="0 0 16 16"><circle cx="8" cy="8" r="7" fill="none" stroke="#fff" stroke-width="1.4"/><path d="M5.5 4.5l1.5 0 .6 1.8-.9.8a5 5 0 0 0 2.2 2.2l.8-.9 1.8.6v1.5c-3.5.3-6.3-2.5-6-6z" fill="#fff"/></svg>
    8004172396</div>
  <div class="abs contact contact__web" style="top:631px;left:0;font-size:12.5px">www.brightharborhome.example</div>
</section>

</body>
</html>
```